Website for Plumbing Company, Sir FlowBoiler

I need a 7-page fully HTML-coded website for my plumbing company, Sir FlowBoiler. We specialize in installation, repair, and replacement of both gas and electric water heaters. Although we offer both tankless (on-demand) water heaters and standard (with tank) water heaters, most of our business is related to standard (with tank) water heaters in the USA market.

These are the pages I need:
1. Home page with sections such as About Us, Our Services, Why Choose Us, Testimonials, Location Map (Palm Beach County Florida), Quote Request Form, Join Our Newsletter, Mission Statement, etc.

2. Gas Water Heaters

3. Electric Water Heaters

4. Tankless Water Heaters

5. About Us

6. Contact Us

7. Privacy Policy, Terms & Conditions

Be sure to mention the following points:
1. Same-Day Service
2. Best Price Guarantee
3. 100% Satisfaction Rating
4. 15-Year Warranty on Water Heater & Parts
5. Lifetime Warranty on Workmanship
*All Warranties are Transferrable Upon Home Sale

Once design is selected and finalized, I need the website coded in a standard HTML/CSS and temporarily hosted on your development server so I can see the website functionality that is not observable from screenshots, such as section animations, etc. Once those details are finalized, I will move the source code to my server and complete the project.

Target Market(s)

Residential Home Owners and Business Owners

Industry/Entity Type

Plumbing, Home Services, Remodeling, Construction

Coding

Coded - Design and coding required

Number of Pages Required

5+ page

Colors
0054AA
0677BA
7BADD7
CADEEF
E8F1F8
FFC000
F8CF3A
FAE287
FDF2CF
FEFAEE
EE7325
F08F49
F5BC92
FAE3D3
FDF4ED

Requirements
Must have
• Clean, colorful, and professional

```html
<!DOCTYPE html>
<html lang="en">
<head>
<meta charset="utf-8">
<title>Sir FlowBoiler – Water Heater Installation, Repair &amp; Replacement</title>
<link href="https://fonts.googleapis.com/css2?family=Space+Grotesk:wght@400;500&family=Open+Sans:wght@400;600&display=swap" rel="stylesheet">
<style>
:root{
  --blue:#0054AA;
  --blue-mid:#0677BA;
  --blue-soft:#CADEEF;
  --blue-mist:#E8F1F8;
  --yellow:#FFC000;
  --yellow-soft:#FDF2CF;
  --orange:#EE7325;
  --orange-soft:#FAE3D3;
  --ink:#0f1e2c;
  --paper:#fafcfe;
  --white:#ffffff;
  --muted:#5f6670;
  --line:#dfe8f1;
}
*{margin:0;padding:0;box-sizing:border-box}
html,body{width:690px;height:1200px;overflow:hidden;background:var(--white)}
body{position:relative;font-family:'Open Sans',sans-serif;color:var(--ink)}
.abs{position:absolute}

/* hero */
.hero{left:0;top:0;width:690px;height:388px;background:var(--paper);overflow:hidden}
.hero-wave{left:0;top:0}
.brand{left:54px;top:15px;font-family:'Space Grotesk',sans-serif;font-weight:500;font-size:12px;color:var(--blue);display:flex;align-items:center;gap:5px}
.brand-mark{width:9px;height:9px;border-radius:50%;background:var(--orange)}
.nav{top:17px;right:54px;display:flex;gap:13.5px;font-family:'Space Grotesk',sans-serif;font-size:8.3px;color:var(--blue)}
.nav-rule{left:54px;top:44px;width:582px;height:1px;background:var(--line)}
.hero-title{left:54px;top:136px;font-family:'Space Grotesk',sans-serif;font-size:36px;line-height:43px;color:var(--ink);font-weight:400}
.hero-title span{color:var(--blue)}
.hero-tag{left:54px;top:233px;width:160px;height:26px;background:var(--yellow);font-family:'Space Grotesk',sans-serif;font-size:8.6px;font-weight:500;color:var(--ink);display:flex;align-items:center;justify-content:center}
.hero-block{left:476px;top:90px;width:160px;height:216px;background:var(--blue)}
.hero-photo{left:356px;top:110px;width:240px;height:176px;background:linear-gradient(135deg,#d9dde2,#a7adb3 55%,#4c4f55)}
.slider-dot{left:612px;width:7px;height:7px;border:1px solid var(--white)}
.slider-dot.active{height:13px;background:var(--yellow);border-color:var(--yellow)}
.features{top:328px;left:54px;display:flex}
.feature{width:151px;display:flex;align-items:center;gap:7px;font-family:'Space Grotesk',sans-serif;font-size:9.3px}
.feature-icon{width:17px;height:17px;background:var(--white);border:1px solid var(--blue-soft);display:flex;align-items:center;justify-content:center}

/* about */
.about-map{left:54px;top:431px;width:135px;height:202px;background:linear-gradient(160deg,#CADEEF,#7BADD7 55%,#E8F1F8)}
.map-pin{left:112px;top:508px}
.about-photo-b{left:199px;top:431px;width:135px;height:152px;background:linear-gradient(160deg,#c9ccd0,#8d9298 55%,#e6e8ea)}
.about-badge{left:199px;top:583px;width:135px;height:50px;background:var(--blue);color:var(--white);font-family:'Space Grotesk',sans-serif;font-size:10.5px;line-height:16px;text-align:center;display:flex;align-items:center;justify-content:center}
.section-title{font-family:'Space Grotesk',sans-serif;font-size:18.5px;color:var(--ink);font-weight:400}
.mark{background:var(--yellow-soft);color:var(--blue);padding:1px 4px}
.about-title{left:356px;top:430px}
.about-copy{left:356px;top:475px;width:275px;font-size:7.2px;line-height:11px;color:var(--muted)}
.about-copy p+p{margin-top:10.5px}
.checks{left:356px;top:559px;display:grid;grid-template-columns:144px 144px;row-gap:7px;font-family:'Space Grotesk',sans-serif;font-size:7.3px}
.checks li{list-style:none;display:flex;align-items:center;gap:4px}
.btn-read{left:356px;top:606px;width:59px;height:17px;background:var(--orange);color:var(--white);font-size:7px;display:flex;align-items:center;justify-content:center}
.social{top:606px;width:17px;height:17px;border:1px solid var(--blue)}

/* why */
.why-title{left:0;top:676px;width:690px;text-align:center}
.why-item{width:190px;text-align:center}
.why-item svg{display:block;margin:0 auto}
.why-item h3{font-family:'Space Grotesk',sans-serif;font-weight:400;font-size:11px;margin-top:8px;color:var(--ink)}
.why-item p{font-size:7px;line-height:11px;color:var(--muted);margin-top:4px}

/* services */
.services-panel{left:54px;top:975px;width:243px;height:225px;background:var(--blue);color:var(--white)}
.services-title{left:22px;top:70px;font-family:'Space Grotesk',sans-serif;font-size:18.5px}
.services-title .mark{padding:1px 4px}
.services-count{left:22px;top:122px;font-family:'Space Grotesk',sans-serif;font-size:10.5px;display:flex;align-items:baseline;gap:4px}
.services-count b{font-size:30px;font-weight:400;color:var(--yellow)}
.service{width:113px;height:113px;color:var(--white);overflow:hidden}
.service-name{position:absolute;left:11px;bottom:22px;font-family:'Space Grotesk',sans-serif;font-size:10.5px}
.service-note{position:absolute;left:11px;bottom:10px;font-size:6.3px}
</style>
</head>
<body>

<section class="abs hero">
  <svg class="abs hero-wave" width="690" height="388" viewBox="0 0 690 388" aria-hidden="true">
    <path d="M355 0 L690 0 L690 388 L335 388 C330 360 345 330 370 300 C300 305 200 290 150 305 C80 320 30 325 0 322 L0 300 C90 280 160 250 200 190 C230 130 230 110 275 90 C320 60 340 30 355 0 Z" fill="#E8F1F8"/>
    <path d="M640 0 L690 0 L690 60 C670 90 655 110 638 118 C650 80 660 40 640 0 Z" fill="#CADEEF"/>
  </svg>
  <div class="abs brand"><span class="brand-mark"></span>Sir FlowBoiler</div>
  <nav class="abs nav"><span>Home</span><span>Services ▾</span><span>About Us</span><span>Privacy Policy</span><span>Terms &amp; Conditions</span><span>Contact</span></nav>
  <div class="abs nav-rule"></div>
  <h1 class="abs hero-title">We are <span>Sir</span><br><span>FlowBoiler</span></h1>
  <div class="abs hero-tag">Request a Free Quote</div>
  <div class="abs hero-block"></div>
  <div class="abs hero-photo" role="img" aria-label="Technician installing a standard tank water heater"></div>
  <div class="abs slider-dot" style="top:180px"></div>
  <div class="abs slider-dot" style="top:191px"></div>
  <div class="abs slider-dot active" style="top:203px"></div>
  <div class="abs features">
    <div class="feature"><span class="feature-icon"><svg width="9" height="9" viewBox="0 0 9 9"><path d="M4.5 0 C6 2.5 7.5 4 7.5 6 A3 3 0 0 1 1.5 6 C1.5 4 3 2.5 4.5 0 Z" fill="#EE7325"/></svg></span>Gas Water Heaters</div>
    <div class="feature"><span class="feature-icon"><svg width="9" height="9" viewBox="0 0 9 9"><path d="M5 0 L1.5 5 L4 5 L3.5 9 L7.5 3.5 L5 3.5 Z" fill="#FFC000"/></svg></span>Electric Water Heaters</div>
    <div class="feature"><span class="feature-icon"><svg width="9" height="9" viewBox="0 0 9 9"><rect x="1.5" y="0.5" width="6" height="8" rx="1" fill="#0054AA"/><rect x="3" y="2" width="3" height="1" fill="#fff"/></svg></span>Tankless Systems</div>
    <div class="feature"><span class="feature-icon"><svg width="9" height="9" viewBox="0 0 9 9"><path d="M4.5 0 A3 3 0 0 1 7.5 3 C7.5 5 4.5 9 4.5 9 C4.5 9 1.5 5 1.5 3 A3 3 0 0 1 4.5 0 Z" fill="#0054AA"/><circle cx="4.5" cy="3" r="1" fill="#fff"/></svg></span>Palm Beach County</div>
  </div>
</section>

<section>
  <div class="abs about-map" role="img" aria-label="Service area map of Palm Beach County, Florida"></div>
  <svg class="abs map-pin" width="20" height="26" viewBox="0 0 20 26" aria-hidden="true"><path d="M10 0 A10 10 0 0 1 20 10 C20 17 10 26 10 26 C10 26 0 17 0 10 A10 10 0 0 1 10 0 Z" fill="#EE7325"/><circle cx="10" cy="10" r="3.5" fill="#fff"/></svg>
  <div class="abs about-photo-b" role="img" aria-label="New gas water heater installed in a garage"></div>
  <div class="abs about-badge">Award Winning<br>Plumbing Company</div>
  <h2 class="abs section-title about-title"><span class="mark">ABOUT</span> Sir FlowBoiler</h2>
  <div class="abs about-copy">
    <p>We install, repair and replace gas and electric water heaters for homes and businesses across Palm Beach County. Most of our work is on standard tank heaters, and we also fit tankless on-demand units for clients who want hot water without the wait.</p>
    <p>Every job comes with a 15-year warranty on the heater and parts, plus a lifetime warranty on workmanship. All warranties transfer upon home sale.</p>
  </div>
  <ul class="abs checks">
    <li><svg width="8" height="6" viewBox="0 0 8 6"><path d="M1 3 L3 5 L7 1" stroke="#EE7325" stroke-width="1.5" fill="none"/></svg>Same-Day Service</li>
    <li><svg width="8" height="6" viewBox="0 0 8 6"><path d="M1 3 L3 5 L7 1" stroke="#EE7325" stroke-width="1.5" fill="none"/></svg>Best Price Guarantee</li>
    <li><svg width="8" height="6" viewBox="0 0 8 6"><path d="M1 3 L3 5 L7 1" stroke="#EE7325" stroke-width="1.5" fill="none"/></svg>100% Satisfaction</li>
    <li><svg width="8" height="6" viewBox="0 0 8 6"><path d="M1 3 L3 5 L7 1" stroke="#EE7325" stroke-width="1.5" fill="none"/></svg>Licensed Plumbers</li>
  </ul>
  <div class="abs btn-read">Get a Quote</div>
  <div class="abs social" style="left:418px"></div>
  <div class="abs social" style="left:439px"></div>
  <div class="abs social" style="left:460px"></div>
  <div class="abs social" style="left:480px"></div>
</section>

<section>
  <h2 class="abs section-title why-title">Why <span class="mark">CHOOSE US</span></h2>

  <div class="abs why-item" style="left:49px;top:718px">
    <svg width="32" height="36" viewBox="0 0 32 36"><rect x="0" y="4" width="32" height="32" rx="3" fill="#0054AA"/><rect x="6" y="0" width="4" height="8" rx="1" fill="#0054AA"/><rect x="22" y="0" width="4" height="8" rx="1" fill="#0054AA"/><circle cx="16" cy="22" r="8" fill="#fff"/><path d="M16 17 L16 22 L20 24" stroke="#EE7325" stroke-width="2" fill="none"/></svg>
    <h3>Same-Day Service</h3>
    <p>Call in the morning and a licensed plumber is at your door the same day, ready to restore your hot water fast.</p>
  </div>
  <div class="abs why-item" style="left:250px;top:718px">
    <svg width="38" height="36" viewBox="0 0 38 36"><text x="15" y="17" font-family="Space Grotesk,sans-serif" font-size="19" font-weight="500" fill="#EE7325">$</text><path d="M0 28 L8 24 C12 22 16 24 20 26 L26 26 L34 20 C37 19 38 22 36 24 L26 33 L10 33 L0 36 Z" fill="#0054AA"/></svg>
    <h3>Best Price Guarantee</h3>
    <p>Found a lower written quote for the same water heater work? We will match it, with no hidden fees or surprises.</p>
  </div>
  <div class="abs why-item" style="left:451px;top:718px">
    <svg width="32" height="36" viewBox="0 0 32 36"><circle cx="16" cy="9" r="9" fill="#0054AA"/><path d="M0 36 C0 26 6 21 16 21 C26 21 32 26 32 36 Z" fill="#0054AA"/><circle cx="26" cy="26" r="6" fill="#FFC000"/></svg>
    <h3>100% Satisfaction Rating</h3>
    <p>Every homeowner and business we serve rates us top marks, and we stay until the job meets your standard.</p>
  </div>

  <div class="abs why-item" style="left:49px;top:836px">
    <svg width="30" height="36" viewBox="0 0 30 36"><path d="M15 0 L30 6 L30 16 C30 26 23 33 15 36 C7 33 0 26 0 16 L0 6 Z" fill="#0054AA"/><text x="15" y="22" text-anchor="middle" font-family="Space Grotesk,sans-serif" font-size="11" font-weight="500" fill="#FFC000">15</text></svg>
    <h3>15-Year Warranty</h3>
    <p>Your new water heater and all of its parts are covered for fifteen full years from the day we install it.</p>
  </div>
  <div class="abs why-item" style="left:250px;top:836px">
    <svg width="36" height="36" viewBox="0 0 36 36"><path d="M3 18 L13 28 L33 8" stroke="#0054AA" stroke-width="6" stroke-linecap="round" stroke-linejoin="round" fill="none"/></svg>
    <h3>Lifetime Workmanship</h3>
    <p>Our installation and repair work is guaranteed for life, so you never pay twice for the same service.</p>
  </div>
  <div class="abs why-item" style="left:451px;top:836px">
    <svg width="36" height="36" viewBox="0 0 36 36"><path d="M18 2 L35 17 L30 17 L30 34 L6 34 L6 17 L1 17 Z" fill="#0054AA"/><rect x="14" y="22" width="8" height="12" fill="#EE7325"/></svg>
    <h3>Transferable Warranties</h3>
    <p>Selling your home? Every warranty we provide moves to the new owner, adding real value at closing.</p>
  </div>
</section>

<section>
  <div class="abs services-panel">
    <h2 class="abs services-title">Our Heater <span class="mark">SERVICES</span></h2>
    <div class="abs services-count"><b>6</b>water heater services</div>
  </div>
  <div class="abs service" style="left:297px;top:975px;background:linear-gradient(180deg,#F5BC92,#F08F49 55%,#0054AA)" role="img" aria-label="Gas water heater">
    <span class="service-name">Gas Heaters</span><span class="service-note">Tank &amp; Standard</span></div>
  <div class="abs service" style="left:410px;top:975px;background:linear-gradient(180deg,#FAE287,#F8CF3A 50%,#0054AA)" role="img" aria-label="Electric water heater">
    <span class="service-name">Electric Heaters</span><span class="service-note">Tank &amp; Standard</span></div>
  <div class="abs service" style="left:523px;top:975px;background:linear-gradient(180deg,#CADEEF,#7BADD7 50%,#0054AA)" role="img" aria-label="Tankless water heater">
    <span class="service-name">Tankless</span><span class="service-note">On-Demand Units</span></div>
  <div class="abs service" style="left:297px;top:1088px;background:linear-gradient(180deg,#7BADD7,#0677BA 55%,#0054AA)" role="img" aria-label="Water heater installation">
    <span class="service-name">Installation</span><span class="service-note">Homes &amp; Business</span></div>
  <div class="abs service" style="left:410px;top:1088px;background:linear-gradient(180deg,#FAE3D3,#EE7325 55%,#0054AA)" role="img" aria-label="Water heater repair">
    <span class="service-name">Repair</span><span class="service-note">Same-Day Service</span></div>
  <div class="abs service" style="left:523px;top:1088px;background:linear-gradient(180deg,#FDF2CF,#FFC000 50%,#0054AA)" role="img" aria-label="Water heater replacement">
    <span class="service-name">Replacement</span><span class="service-note">Best Price Guarantee</span></div>
</section>

</body>
</html>
```